Veltrix Project

Project Description
This presentation is to Veltrix (www.veltrix-care.example)
We are a physician’s group practice that is trying to convince Veltrix that we have the systems in place to service their clients in Assisted Living Facilities. (ALF’s)
We have to convince them in this presentation, that we have controls in place to curtail over utilization of services in general and more specifically averting clients from using the Emergency room as their primary care provider. I've included the content that needs to be included in the slides. We need to document and graphically display the message that we can effectively manage their patients in this unique environment of Assisted Living Facilities.
We also have a unique opportunity to bring some new business on board if we get this contract. We may be able to bring several thousand patients unto Veltrix who previously weren’t enrolled with the carrier. We’d like to highlight that opportunity using some type of graphic art.

My presentation is due Friday, August 21, 2012.

Target Market(s)

Medical Directors (Physicians) and Health Care Attorneys

Industry/Entity Type

Environment

Requirements
Must have
• Graphics that mirror the message
Should not have
• Veltrix Logo.

```html
<!DOCTYPE html>
<html lang="en">
<head>
<meta charset="utf-8">
<title>Crestline Mobile Health Solutions — Veltrix Presentation</title>
<link href="https://fonts.googleapis.com/css2?family=Questrial&family=Open+Sans:wght@400;600;700&display=swap" rel="stylesheet">
<style>
:root{
  --backdrop:#5b5b5b;
  --teal:#1fb0a3;
  --teal-mid:#1590a6;
  --blue:#0b5aa6;
  --navy:#0b3f7a;
  --ink:#55606a;
  --paper:#ffffff;
  --soft:#eef3f5;
  --photo-warm:#d9cbbd;
  --photo-cool:#c9d3da;
}
*{box-sizing:border-box;margin:0;padding:0}
html,body{width:800px;height:1200px;overflow:hidden;background:var(--backdrop)}
body{position:relative;font-family:"Open Sans",sans-serif}
.slide{position:absolute;width:254px;height:190px;background:var(--paper);overflow:hidden}
.c1{left:10px}.c2{left:274px}.c3{left:536px}
.r1{top:12px}.r2{top:210px}.r3{top:406px}.r4{top:604px}.r5{top:802px}.r6{top:1000px}
.c6a{left:138px}.c6b{left:402px}

.photo{position:absolute;background:linear-gradient(160deg,var(--photo-cool),var(--photo-warm))}
.grad{position:absolute;background:linear-gradient(200deg,var(--teal) 0%,var(--teal-mid) 45%,var(--blue) 100%)}
.section-label{position:absolute;right:0;bottom:0;color:#fff;font-family:"Questrial",sans-serif;font-size:16px;line-height:1.1;text-align:right;letter-spacing:.2px}

.header{position:absolute;left:0;top:0;width:100%;height:22px;background:linear-gradient(90deg,var(--teal-mid),#1b9da3 60%,#2bb4a8);border-bottom:2px solid #d7ecef;color:#fff;font-family:"Questrial",sans-serif;font-size:10.5px;line-height:21px;padding-left:6px;letter-spacing:.2px}
.header small{font-size:5px}
.bullets{position:absolute;left:10px;right:12px;top:30px;list-style:none}
.bullets li{position:relative;padding-left:10px;font-size:5.2px;line-height:1.55;color:var(--ink);margin-bottom:4.6px}
.bullets li::before{content:"";position:absolute;left:0;top:1.6px;width:4.5px;height:4.5px;border-radius:50%;background:var(--teal-mid)}
.bullets b{color:var(--blue)}
.mark{position:absolute;right:4px;bottom:3px;display:flex;align-items:center;gap:2px;font-size:4px;color:var(--blue);font-weight:700}
.mark i{width:4px;height:4px;border-radius:50%;background:var(--blue)}

/* title */
.title-band{position:absolute;left:0;bottom:0;width:100%;height:56px;background:#fff;border-top:2px solid var(--teal-mid)}
.brand{position:absolute;left:10px;top:14px;display:flex;align-items:center;gap:4px;font-family:"Questrial",sans-serif;font-size:8.5px;color:var(--blue)}
.brand i{width:8px;height:8px;border-radius:50%;background:var(--blue)}
.title-text{position:absolute;right:8px;top:18px;font-family:"Questrial",sans-serif;font-size:10.5px;color:var(--teal-mid)}
.thanks{font-size:17px;top:10px}

/* TOC */
.pill{position:absolute;height:10px;border-radius:3px;background:linear-gradient(90deg,var(--teal-mid),var(--teal));color:#fff;font-size:4.3px;line-height:10px;padding:0 8px;border:1px solid #fff;box-shadow:0 1px 2px rgba(0,0,0,.2)}

/* services */
.svc{position:absolute;width:46px;height:46px}
.svc-tag{position:absolute;height:7px;background:var(--teal-mid);color:#fff;font-size:3.3px;line-height:7px;padding:0 3px;white-space:nowrap}

/* hospitalization */
.stage{position:absolute;left:18px;width:52px;height:38px}
.stage-label{position:absolute;left:18px;width:44px;color:#fff;font-size:4.3px;text-align:center}
.stage-box{position:absolute;left:60px;width:186px;border-radius:4px;background:linear-gradient(90deg,#1e9fb0,var(--teal));color:#fff;font-size:2.8px;line-height:1.35;padding:2px 4px}

/* wheel */
.note{position:absolute;width:54px;height:40px;border:1px solid var(--teal-mid);border-radius:4px;font-size:3.2px;color:var(--blue);padding:2px 3px;line-height:1.4;background:#fff}
.q{position:absolute;font-size:5.3px;color:#fff;font-weight:700;text-align:center;line-height:1.2}

/* network */
.who{position:absolute;width:14px;height:14px;border-radius:3px;background:linear-gradient(180deg,#8fa6bd,#4d6f93)}
.tag{position:absolute;height:6px;background:var(--blue);color:#fff;font-size:3.4px;line-height:6px;padding:0 3px;border:1px solid #fff;white-space:nowrap}
</style>
</head>
<body>

<!-- Title -->
<section class="slide c1 r1">
  <div class="photo" style="left:0;top:0;width:100%;height:134px" role="img" aria-label="Collage of nurses caring for elderly patients"></div>
  <div class="title-band">
    <div class="brand"><i></i>CRESTLINE</div>
    <div class="title-text">PRESENTATION TITLE</div>
  </div>
</section>

<!-- Table of contents -->
<section class="slide c2 r1">
  <div class="photo" style="left:0;top:22px;width:100%;height:168px;opacity:.45" role="img" aria-label="Faded photo of a caregiver with a senior patient"></div>
  <div class="header">TABLE OF CONTENTS</div>
  <div class="pill" style="left:3px;top:33px">ABOUT US</div>
  <div class="pill" style="left:19px;top:54px">SERVICES OFFERED</div>
  <div class="pill" style="left:88px;top:78px">ABOUT TAPS</div>
  <div class="pill" style="left:104px;top:98px">ALF SERVICES</div>
  <div class="pill" style="left:170px;top:126px">WHY US ?</div>
  <div class="pill" style="left:188px;top:147px;line-height:5px;font-size:3.8px;padding:1px 8px;height:13px;text-align:center">MUTUAL BUSINESS<br>BENEFIT</div>
  <div class="mark"><i></i>CRESTLINE</div>
</section>

<!-- About us section -->
<section class="slide c3 r1">
  <div class="grad" style="inset:0"></div>
  <div class="photo" style="left:0;top:0;width:130px;height:190px" role="img" aria-label="Portrait of a smiling physician in a white coat"></div>
  <div class="section-label">ABOUT US</div>
</section>

<!-- About us content -->
<section class="slide c1 r2">
  <div class="header">ABOUT US</div>
  <ul class="bullets">
    <li>Crestline Mobile Health Solutions is an all encompassing, comprehensive solution for all healthcare needs.</li>
    <li>We help improve the well being of homebound patients by providing high quality, personalized and confidential medical care.</li>
    <li>We believe in the synergy of encouraging our patients and their caregivers to be part of the treatment plan to achieve a much better outcome.</li>
    <li>We provide our patients with all the necessary care coordination in order to access all the community resources that are available to our home bound patients.</li>
    <li>We have a strong network of highly trained licensed physicians and medical providers and all our staffs are pre-screened by SHCA Level - II</li>
    <li>Based in Florida, our service extends to..........</li>
  </ul>
  <div class="mark"><i></i>CRESTLINE</div>
</section>

<!-- Services offered section -->
<section class="slide c2 r2">
  <div class="grad" style="inset:0"></div>
  <div class="photo" style="left:0;top:0;width:127px;height:190px" role="img" aria-label="Caregiver handing flowers to a senior woman"></div>
  <div class="section-label">SERVICES OFFERED</div>
</section>

<!-- Services offered content -->
<section class="slide c3 r2">
  <div class="header" style="background:#fff;color:var(--teal-mid);border-left:3px solid var(--teal-mid);border-bottom:2px solid #dfe9ec">SERVICES OFFERED</div>
  <div class="svc photo" style="left:3px;top:38px" role="img" aria-label="Physician consulting a patient"></div>
  <div class="svc-tag" style="left:3px;top:94px">PHYSICIAN SERVICES</div>
  <div class="svc photo" style="left:53px;top:52px" role="img" aria-label="Nurse at a patient's home"></div>
  <div class="svc-tag" style="left:53px;top:108px">MEDICAL HOME SERVICE</div>
  <div class="svc photo" style="left:103px;top:66px" role="img" aria-label="Dentist treating a patient"></div>
  <div class="svc-tag" style="left:103px;top:122px">DENTAL SERVICES</div>
  <div class="svc photo" style="left:153px;top:80px" role="img" aria-label="Doctor holding a chart"></div>
  <div class="svc-tag" style="left:153px;top:136px;line-height:3.5px;height:9px">POSTDISCHARGE<br>MAINTENANCE PROGRAM</div>
  <div class="svc photo" style="left:203px;top:96px" role="img" aria-label="Doctor on the phone"></div>
  <div class="svc-tag" style="left:208px;top:152px">TAPS PROGRAM</div>
  <div class="mark"><i></i>CRESTLINE</div>
</section>

<!-- About TAPS section -->
<section class="slide c1 r3">
  <div class="grad" style="inset:0"></div>
  <div class="photo" style="left:0;top:0;width:127px;height:190px" role="img" aria-label="Senior woman seated in a wheelchair"></div>
  <div class="section-label">ABOUT TAPS</div>
</section>

<!-- About TAPS content -->
<section class="slide c2 r3">
  <div class="header">ABOUT TAPS <small>(Total ALF Partner Solution)</small></div>
  <ul class="bullets" style="top:66px">
    <li>TAPS is a program established to promote communication for the continuity of care between physicians, rehabs, hospitals and hospices.</li>
    <li>We serve as a bridge by working closely with our related partners.</li>
    <li>We ensure the best care and a smooth transition of the patient to the appropriate medical establishment and back home.</li>
  </ul>
  <div class="mark"><i></i>CRESTLINE</div>
</section>

<!-- ALF services section -->
<section class="slide c3 r3">
  <div class="grad" style="inset:0"></div>
  <div class="photo" style="left:0;top:0;width:127px;height:190px" role="img" aria-label="Nurse pushing a senior in a wheelchair down a corridor"></div>
  <div class="section-label">ALF SERVICES</div>
</section>

<!-- ALF services content -->
<section class="slide c1 r4">
  <div class="header">ALF SERVICES</div>
  <ul class="bullets" style="top:32px">
    <li>We have a strong team of physicians, assistants, nurses who with their expertise and flexibility gives ALF an excellent choice to address their needs</li>
    <li>Our competence lies in responding quickly to new referrals and more urgent care environments</li>
    <li>We serve as a bridge working with several hospitals, Rehabs, Hospices to communicate regarding the patients continuity of care.</li>
    <li>Routine visits ensures happy residents as it required fewer hospital and ER visits</li>
    <li>We employ state of the art electronic medical record system which stores the complete details of the residents</li>
    <li>Details are sent to Medical Professionals for review and when necessary, we coordinate with the ALF to arrange for additional services like laboratory testing, diagnostics etc.,</li>
  </ul>
  <div class="mark"><i></i>CRESTLINE</div>
</section>

<!-- Why us section -->
<section class="slide c2 r4">
  <div class="grad" style="inset:0"></div>
  <div class="photo" style="left:0;top:0;width:127px;height:190px" role="img" aria-label="Team of smiling doctors and nurses"></div>
  <div class="section-label">WHY US</div>
</section>

<!-- Why us content -->
<section class="slide c3 r4">
  <div class="header">WHY US</div>
  <ul class="bullets" style="top:32px">
    <li>We work closely with ALF's and ensure that all the medical needs of the inmates are met</li>
    <li>Our strong team of physicians, assistants, nurses and counselors deliver an integrated holistic approach to healthcare. <b>24 HRS COVERAGE</b></li>
    <li>Our team visits ALF on a regular basis thereby developing a one-to-one relationship with them and better addressing their health needs</li>
    <li>Every visit includes review of current medical concerns and medications as well as preventive care which ensures lesser visits to hospitals and ER and moreover better health.</li>
    <li>Our state of the art electronic medical records helps us keep track of the patients health and also keeps all those related to the patient updated with the developements</li>
  </ul>
  <div class="mark"><i></i>CRESTLINE</div>
</section>

<!-- Hospitalization avoidance -->
<section class="slide c1 r5">
  <div class="header">WHY US – HOSPITALIZATION AVOIDANCE</div>
  <svg width="254" height="190" style="position:absolute;left:0;top:0">
    <defs><linearGradient id="chev" x1="0" y1="0" x2="0" y2="1"><stop offset="0" stop-color="#1f7fc0"/><stop offset="1" stop-color="#0b3f7a"/></linearGradient></defs>
    <path d="M20 28 H64 V66 L42 74 L20 66 Z" fill="url(#chev)"/>
    <path d="M20 76 H64 V100 L42 108 L20 100 Z" fill="url(#chev)"/>
    <path d="M20 110 H64 V134 L42 142 L20 134 Z" fill="url(#chev)"/>
    <path d="M20 144 H64 V176 H20 Z" fill="url(#chev)"/>
  </svg>
  <div class="stage-label" style="top:47px">PREVENTION</div>
  <div class="stage-label" style="top:89px">DIVERSION</div>
  <div class="stage-label" style="top:119px">PATIENT<br>TRACKING</div>
  <div class="stage-label" style="top:155px">POST<br>HOSPITALIZATION</div>
  <div class="stage-box" style="top:30px;height:42px">•Emergency response button – calls our office before any 911 call<br>•24 hr. on call medical &amp; physician staff<br>•Patient centered medical home to triage ALF complaints<br>•Frequent facility visits – once a month and as needed<br>•Telemedicine triage of patients assessing need for a visit<br>•Medicine treatment protocols – staff physician<br>•Psychiatric treatment protocols – staff specialist<br>•Psychiatric rapid intervention team</div>
  <div class="stage-box" style="top:78px;height:24px">•Direct communication with ER physician about pending case<br>•Discuss treatment needs limiting treatment to emergent care<br>•Daily telephone f/u with hospital and our physician</div>
  <div class="stage-box" style="top:112px;height:24px">•Advanced patient tracking (hospital, SNF, ALF)<br>•Direct connection to the hospital – real time medical history<br>•Discharge planning for current hospitalized case – evaluate outpatient options</div>
  <div class="stage-box" style="top:146px;height:24px">•Tracking patients through the SNF and back to the ALF<br>•Immediate clinical follow up within 24-48 hrs<br>•Avoiding future admissions using aggressive protocols</div>
  <div class="mark"><i></i>CRESTLINE</div>
</section>

<!-- Mutual business benefit section -->
<section class="slide c2 r5">
  <div class="grad" style="inset:0"></div>
  <div class="photo" style="left:0;top:0;width:127px;height:190px" role="img" aria-label="Close-up of a thumbs-up hand"></div>
  <div class="section-label">MUTUAL BUSINESS<br>BENEFIT</div>
</section>

<!-- Mutual business benefit wheel -->
<section class="slide c3 r5">
  <div class="header">MUTUAL BUSINESS BENEFIT</div>
  <svg width="254" height="190" style="position:absolute;left:0;top:0">
    <defs><linearGradient id="wheel" x1="0" y1="0" x2="1" y2="1"><stop offset="0" stop-color="#2bb5a5"/><stop offset="1" stop-color="#0b5aa6"/></linearGradient></defs>
    <circle cx="128" cy="102" r="62" fill="url(#wheel)"/>
    <line x1="128" y1="40" x2="128" y2="164" stroke="#fff" stroke-width="2.5"/>
    <line x1="66" y1="102" x2="190" y2="102" stroke="#fff" stroke-width="2.5"/>
    <circle cx="128" cy="102" r="6" fill="none" stroke="#fff" stroke-width="1.5"/>
    <path d="M60 58 H78 V72" fill="none" stroke="#1590a6" stroke-width=".8"/>
    <path d="M60 150 H80 V140" fill="none" stroke="#1590a6" stroke-width=".8"/>
    <path d="M196 150 H176 V140" fill="none" stroke="#1590a6" stroke-width=".8"/>
  </svg>
  <div class="note" style="left:4px;top:34px">• Additional Revenue<br>• Better Coordination<br>• Better Outcomes</div>
  <div class="note" style="left:4px;top:128px">• Sub-Acute Care Provider: SNF setting referring back to you</div>
  <div class="note" style="left:196px;top:128px">Acute Care Provider: Hospital setting referring back to you</div>
  <div class="q" style="left:84px;top:66px;width:40px">Continuum<br>of Care:<br>ACO<br>Model</div>
  <div class="q" style="left:132px;top:66px;width:44px">Crestline<br>MHS<br>Visiting<br>Physicians</div>
  <div class="q" style="left:84px;top:110px;width:40px">Harborview<br>Care</div>
  <div class="q" style="left:132px;top:112px;width:44px">Northgate<br>Facility</div>
  <div class="mark"><i></i>CRESTLINE</div>
</section>

<!-- Mutual business benefit network -->
<section class="slide c6a r6">
  <div class="header">MUTUAL BUSINESS BENEFIT</div>
  <svg width="254" height="190" style="position:absolute;left:0;top:0">
    <g fill="none" stroke="#3d7fb8" stroke-width=".6" stroke-dasharray="2 1.5">
      <path d="M125 68 Q70 80 38 130"/>
      <path d="M125 68 Q95 95 62 152"/>
      <path d="M125 68 Q118 110 104 172"/>
      <path d="M125 68 Q160 110 152 172"/>
      <path d="M125 68 Q180 90 190 146"/>
      <path d="M125 68 Q200 75 218 126"/>
      <path d="M128 102 Q60 100 38 130"/>
      <path d="M128 102 Q200 100 218 126"/>
      <path d="M128 112 L104 172"/>
      <path d="M128 112 L152 172"/>
    </g>
  </svg>
  <div class="who" style="left:118px;top:40px;width:26px;height:20px" role="img" aria-label="Client business people"></div>
  <div class="tag" style="left:116px;top:62px">CLIENT</div>
  <div class="who" style="left:116px;top:92px;width:26px;height:22px" role="img" aria-label="Medical team at the centre"></div>
  <div class="tag" style="left:118px;top:116px">CMHS</div>
  <div class="who" style="left:30px;top:118px" role="img" aria-label="Patient"></div>
  <div class="tag" style="left:22px;top:134px">PATIENT-1</div>
  <div class="who" style="left:56px;top:140px" role="img" aria-label="Patient"></div>
  <div class="tag" style="left:52px;top:156px">PATIENT-2</div>
  <div class="who" style="left:98px;top:160px" role="img" aria-label="Patient"></div>
  <div class="tag" style="left:94px;top:176px">PATIENT-3</div>
  <div class="who" style="left:146px;top:160px" role="img" aria-label="Patient"></div>
  <div class="tag" style="left:140px;top:176px">PATIENT-4</div>
  <div class="who" style="left:184px;top:134px" role="img" aria-label="Patient"></div>
  <div class="tag" style="left:178px;top:150px">PATIENT-5</div>
  <div class="who" style="left:212px;top:112px" role="img" aria-label="Patient"></div>
  <div class="tag" style="left:206px;top:128px">PATIENT-6</div>
  <div class="mark"><i></i>CRESTLINE</div>
</section>

<!-- Thank you -->
<section class="slide c6b r6">
  <div class="photo" style="left:0;top:0;width:100%;height:134px" role="img" aria-label="Collage of nurses caring for elderly patients"></div>
  <div class="title-band">
    <div class="brand"><i></i>CRESTLINE</div>
    <div class="title-text thanks">THANK YOU</div>
  </div>
</section>

</body>
</html>
```